Ridgeline Orchards Organic Cherry POS card 7x11

We are wanting to create a one-sided 7 x 11 organic cherry card that is eye catching and informative.This should be clear and easy to read and not cluttered. We use these cards as a display in grocery stores, demo stands, and other events to market Organic Ridgeline Sweet Orchards. We have a few facts that we would like displayed on the card (see attachment).

Target Market(s)

Consumers

Industry/Entity Type

Agriculture

Requirements
Must have
• Natural color palettes
• Easy to read
• Ridgeline Orchards
Nice to have
• Unique, realistic cherry design

```html
<!DOCTYPE html>
<html lang="en">
<head>
<meta charset="utf-8">
<title>Ridgeline Orchards – Organic Cherry Card</title>
<link href="https://fonts.googleapis.com/css2?family=Roboto:wght@300;400;700&display=swap" rel="stylesheet">
<style>
  :root {
    --bg-left: #5c2a2b;
    --bg-mid: #4a2226;
    --bg-right: #3b1a20;
    --band-left: #4e1a20;
    --band-mid: #6e1620;
    --band-right: #8d111b;
    --photo-light: #8a1019;
    --photo-dark: #3e0608;
    --white: #ffffff;
    --logo-ink: #4a1b1e;
  }
  * { margin: 0; padding: 0; box-sizing: border-box; }
  html, body { width: 1200px; height: 764px; overflow: hidden; background: var(--bg-right); }
  .card {
    position: relative;
    width: 1200px;
    height: 764px;
    overflow: hidden;
    background: linear-gradient(90deg, var(--bg-left) 0%, var(--bg-mid) 50%, var(--bg-right) 100%);
    font-family: "Roboto", Arial, sans-serif;
    color: var(--white);
  }
  .feature-band {
    position: absolute;
    left: 600px;
    top: 336px;
    width: 600px;
    height: 376px;
    background: linear-gradient(90deg, var(--band-left) 0%, var(--band-mid) 50%, var(--band-right) 100%);
  }
  .cherry-photo {
    position: absolute;
    left: 70px;
    top: 70px;
    width: 640px;
    height: 640px;
    border-radius: 50%;
    background: linear-gradient(135deg, var(--photo-light) 0%, var(--photo-dark) 100%);
  }
  .brand-tag {
    position: absolute;
    left: 912px;
    top: 79px;
    width: 205px;
    height: 73px;
    background: var(--white);
    display: flex;
    align-items: center;
    justify-content: center;
    gap: 10px;
  }
  .brand-dot {
    width: 18px;
    height: 18px;
    border-radius: 50%;
    background: var(--logo-ink);
  }
  .brand-name {
    font-weight: 400;
    font-size: 20px;
    color: var(--logo-ink);
  }
  .fact-lead {
    position: absolute;
    right: 76px;
    top: 200px;
    width: 460px;
    text-align: right;
    font-weight: 300;
    font-size: 26px;
    line-height: 34px;
  }
  .fact-frame {
    position: absolute;
    left: 436px;
    top: 379px;
    width: 693px;
    height: 147px;
    border: 2px solid var(--white);
    display: flex;
    align-items: center;
    justify-content: flex-end;
    padding-right: 38px;
  }
  .fact-headline {
    text-align: right;
    text-transform: uppercase;
    font-weight: 700;
    font-size: 27px;
    line-height: 35px;
    letter-spacing: 0.2em;
  }
  .benefits {
    position: absolute;
    right: 71px;
    top: 603px;
    text-align: right;
  }
  .benefits-title {
    font-weight: 700;
    font-size: 23px;
    line-height: 28px;
  }
  .benefits-list {
    font-weight: 300;
    font-size: 16.5px;
    line-height: 24px;
  }
</style>
</head>
<body>
  <main class="card">
    <div class="feature-band"></div>
    <div class="cherry-photo" role="img" aria-label="Close-up photograph of glossy ripe red cherries with green stems"></div>

    <div class="brand-tag">
      <span class="brand-dot"></span>
      <span class="brand-name">Ridgeline Orchards</span>
    </div>

    <p class="fact-lead">Washington State is the<br>nation’s largest producer of<br>organic cherries.</p>

    <div class="fact-frame">
      <h1 class="fact-headline">Organic Ridgeline Cherries<br>make up 1/3 of the<br>nation’s production.</h1>
    </div>

    <section class="benefits">
      <h2 class="benefits-title">Health benefits:</h2>
      <p class="benefits-list">Fat Free | Source of Vitamin C | A Natural Anti-Inflammatory<br>Source of Potassium | Source of Melatonin</p>
    </section>
  </main>
</body>
</html>
```